Design business card using existing logo.

PLEASE DO NOT USE "RED WHITE & BLACK" color combo! Thank you.

Try different color combos such as:
- Vintage colors like brown, orange, gold, blue (not all together but a combo of 1 or 3
- Blue, w/ grey, or silver or white, Blue monochromatic can work as well.
- Use monochromatic variations on back (just an idea)

- Include full name, "Quillmark Records" on at least one side.

Target Market(s)

Teens

Industry/Entity Type

Business

Colors
3277b5
ffc214
f04a50
f78f20

```html
<!DOCTYPE html>
<html lang="en">
<head>
<meta charset="utf-8">
<title>Quillmark Records – Business Card</title>
<link href="https://fonts.googleapis.com/css2?family=Montserrat:wght@700&family=Antonio:wght@200&display=swap" rel="stylesheet">
<style>
  :root{
    --backdrop:#e9e4de;
    --yellow:#f1d417;
    --amber:#efb15c;
    --coral:#eb6a4b;
    --blue:#5a87c6;
    --violet:#a35aa2;
    --teal:#6cbfae;
    --slate:#4b4b4e;
    --ink:#2a2a2c;
    --paper:#ffffff;
  }
  *{box-sizing:border-box;margin:0;padding:0}
  html,body{width:1200px;height:891px;overflow:hidden;background:var(--backdrop)}
  .canvas{position:relative;width:1200px;height:891px}
  .card{position:absolute;top:297px;width:520px;height:297px;overflow:hidden;
        box-shadow:0 6px 18px rgba(0,0,0,.18)}
  .card__art{position:absolute;inset:0}
  .card--front{left:50px}
  .card--front .card__art{
    background:linear-gradient(125deg,var(--coral) 0%,var(--amber) 40%,var(--yellow) 75%,var(--teal) 100%);
  }
  .card--back{left:630px}
  .card--back .card__art{
    background:linear-gradient(125deg,var(--teal) 0%,var(--slate) 45%,var(--violet) 80%,var(--blue) 100%);
  }

  .brand{position:absolute;left:0;right:0;top:125px;display:flex;align-items:center;justify-content:center;gap:16px}
  .brand__dot{width:44px;height:44px;border-radius:50%;background:var(--ink);flex:none}
  .brand__name{font-family:"Montserrat",sans-serif;font-weight:700;font-size:44px;letter-spacing:1px;color:var(--ink);line-height:1}

  .title{position:absolute;left:50px;right:50px;top:104px;text-align:center}
  .title__rule{height:1.5px;background:var(--paper)}
  .title__rule--top{margin:0 20px 12px 20px}
  .title__rule--bottom{margin:12px 20px 0 20px}
  .title__text{font-family:"Antonio",sans-serif;font-weight:200;font-size:50px;line-height:1;color:var(--paper);letter-spacing:1px;white-space:nowrap}
</style>
</head>
<body>
<main class="canvas">

  <section class="card card--front" aria-label="Card front">
    <div class="card__art" role="img" aria-label="Overlapping multicolour geometric block pattern in coral, amber, yellow and teal"></div>
    <div class="brand">
      <span class="brand__dot"></span>
      <span class="brand__name">QUILLMARK</span>
    </div>
  </section>

  <section class="card card--back" aria-label="Card back">
    <div class="card__art" role="img" aria-label="Overlapping multicolour geometric block pattern in teal, slate, violet and blue"></div>
    <div class="title">
      <div class="title__rule title__rule--top"></div>
      <h1 class="title__text">QUILLMARK RECORDS</h1>
      <div class="title__rule title__rule--bottom"></div>
    </div>
  </section>

</main>
</body>
</html>
```